TW Groundworks Capability Statement

I need to design a two page Capability statement for our Civil Construction company that looks professional and can be issued to clients in electronic or print form to show our capabilities.

We have an existing Logo and website https://twgroundworks.com.au/

It should include space for the below:
- Company heading/logo plus ABN, ACN and full contact details
- About Us – Mission, vision, values
- Our Service Offering / Core competencies
- Accreditations/certifications

Designs look the same

```html
<!DOCTYPE html>
<html lang="en">
<head>
<meta charset="utf-8">
<title>TW Groundworks – Capability Statement</title>
<link href="https://fonts.googleapis.com/css2?family=Anton&family=Montserrat:wght@400;500;600;700;800&family=Oswald:wght@500;600&display=swap" rel="stylesheet">
<style>
:root{
  --navy:#25226e;
  --navy-mid:#2f2c86;
  --band:#3b3fae;
  --yellow:#f0b323;
  --ink:#2a2a2a;
  --backdrop:#b3b3b3;
  --white:#ffffff;
}
*{margin:0;padding:0;box-sizing:border-box}
html,body{width:1200px;height:1117px;overflow:hidden;background:var(--backdrop)}
body{position:relative;font-family:"Montserrat",sans-serif;color:var(--ink)}
.page{position:absolute;top:178px;width:539px;height:761px;background:var(--white);overflow:hidden}
.page-front{left:50px}
.page-back{left:613px}
.shape{position:absolute;left:0;top:0}

/* front */
.brand{position:absolute;left:340px;top:22px;display:flex;align-items:center;gap:7px;color:var(--navy);font-weight:800;font-size:16px;letter-spacing:-.2px}
.brand-mark{width:22px;height:22px;background:var(--yellow)}
.hero-title{position:absolute;left:34px;top:228px;font-family:"Anton",sans-serif;font-size:40px;line-height:1.05;color:var(--white);letter-spacing:-.3px}
.hero-title .accent{display:block;color:var(--yellow);padding-left:57px}
.about-tag{position:absolute;left:34px;top:399px;width:208px;height:28px;background:var(--yellow);color:var(--white);font-weight:800;font-size:19px;text-align:center;line-height:28px}
.about-lead{position:absolute;left:34px;top:439px;width:212px;font-weight:700;font-size:9.3px;line-height:1.2;color:#111}
.about-body{position:absolute;left:34px;top:485px;width:214px;font-size:8.9px;line-height:1.15;color:#333}
.about-body p+p{margin-top:9px}
.about-column{position:absolute;left:284px;top:358px;width:224px;font-size:8.1px;line-height:10px;letter-spacing:-.1px;color:var(--white);text-align:justify}
.about-column p+p{margin-top:10px}

/* footer */
.call-label{position:absolute;left:34px;top:699px;font-weight:800;font-size:20px;color:var(--yellow)}
.call-rule{position:absolute;left:114px;top:680px;width:1px;height:58px;background:var(--white)}
.phone{position:absolute;left:126px;color:var(--white)}
.phone-num{display:flex;align-items:center;gap:4px;font-family:"Oswald",sans-serif;font-weight:600;font-size:16px;line-height:1}
.phone-name{font-size:9.3px;font-weight:500;margin-top:1px}
.contact-list{position:absolute;left:295px;top:675px;list-style:none;font-size:11.8px;line-height:15.4px;color:#111;font-weight:500}
.contact-list li{display:flex;align-items:flex-start;gap:7px}
.contact-list svg{flex:none;margin-top:3px}
.contact-list .indent{padding-left:17px}

/* back */
.services-bar{position:absolute;left:38px;top:24px;width:463px;height:30px;background:var(--band);color:var(--white);font-weight:800;font-size:20px;text-align:center;line-height:30px}
.svc-col{position:absolute;top:69px}
.svc-col h3{font-size:11px;font-weight:700;color:var(--yellow);margin-bottom:9px}
.svc-col ul{list-style:none}
.svc-col li{position:relative;padding-left:13px;font-size:7.6px;line-height:8.6px;letter-spacing:-.1px;color:var(--white);margin-bottom:8.3px}
.svc-col li::before{content:"";position:absolute;left:0;top:1px;width:6px;height:6px;border:1px solid var(--yellow);border-radius:50%}
.svc-col li::after{content:"";position:absolute;left:2.2px;top:2.4px;width:1.8px;height:3px;border:solid var(--yellow);border-width:0 1px 1px 0;transform:rotate(40deg)}
.why{position:absolute;left:44px;top:362px;width:96px;text-align:center;font-weight:800;font-size:22px;line-height:24px;color:var(--navy)}
.why .accent{color:var(--yellow)}
.why-rule{position:absolute;left:147px;top:356px;width:1.5px;height:93px;background:var(--navy)}
.pillar{position:absolute;top:355px;width:90px;text-align:center}
.pillar-badge{width:68px;height:68px;margin:0 auto;border-radius:50%;background:var(--navy);display:flex;align-items:center;justify-content:center}
.pillar-name{margin-top:6px;font-weight:600;font-size:10px;line-height:11.5px;color:#111}
.pillar-link{position:absolute;top:388px;width:14px;border-top:1.5px dotted var(--yellow)}
.focus-box{position:absolute;left:41px;top:472px;width:456px;height:175px;border:2.5px solid var(--yellow)}
.focus-rule{position:absolute;left:276px;top:493px;width:1px;height:133px;background:var(--yellow)}
.focus{position:absolute;top:492px;width:208px}
.focus h4{font-weight:800;font-size:15px;color:var(--navy);margin-bottom:4px}
.focus p{font-size:8.1px;line-height:10.2px;letter-spacing:-.1px;color:#333}
</style>
</head>
<body>

<section class="page page-front" aria-label="Capability statement, page one">
  <svg class="shape" width="539" height="761" viewBox="0 0 539 761">
    <defs>
      <linearGradient id="heroTone" x1="0" y1="0" x2="1" y2="1">
        <stop offset="0" stop-color="#4a5a70"/>
        <stop offset=".45" stop-color="#9aa3ae"/>
        <stop offset="1" stop-color="#d9dde2"/>
      </linearGradient>
    </defs>
    <polygon role="img" aria-label="Photo of site engineers reviewing plans beside a white hard hat" points="0,0 281,0 539,48 539,268 158,354 0,304" fill="url(#heroTone)"/>
    <rect x="264" y="290" width="262" height="372" fill="var(--navy)"/>
    <polygon points="0,312 158,362 539,276 539,300 158,386 0,338" fill="var(--navy)"/>
    <polyline points="0,307 158,357 539,271" fill="none" stroke="#fff" stroke-width="3"/>
    <rect x="526" y="290" width="13" height="471" fill="var(--yellow)"/>
    <polygon points="0,660 232,660 275,753 0,753" fill="var(--navy)"/>
    <rect x="0" y="753" width="539" height="8" fill="var(--navy)"/>
  </svg>

  <div class="brand"><span class="brand-mark"></span>TW Groundworks</div>

  <h1 class="hero-title">CIVIL CONTRUCTION<span class="accent">EXCELLENCE</span></h1>

  <div class="about-tag">ABOUT US</div>
  <p class="about-lead">Tier 1 engineering and project management capability with nimble privately owned and operated mentality.</p>
  <div class="about-body">
    <p>Founded by Martin Kell and Daniel Ross, TW Groundworks is a Utilities business focused on underground utilities.</p>
    <p>Martin &amp; Daniel have over 25 years’ combined experience, with the majority of this time being colleagues at national and international engineering services organisations delivering underground utility works. Evolving their careers from graduates to senior managers over seeing program/project budgets greater $100m. TW Groundworks was established through their shared passions for safety, client satisfaction, field productivity and most importantly a positive workplace.</p>
  </div>

  <div class="about-column">
    <p>TW Groundworks leverage our demonstrated experience and countless relationships within the industry to provide market leading service. Our focus is our clients, and finding ways we can make their lives easier. We create a collaborative environment on all our projects by providing as much transparency and visibility as possible which enables us to work together to find mutually beneficial outcomes for all stakeholders. This approach leads to long standing partnerships,and exceptional results for all parties.</p>
    <p>Ensuring Safety is the number one priority isn’t just talk at TW Groundworks. It is an engrained philosophy that we live and breathe every day. We understand and are committed to targeting a generative safety culture. An environment with the appropriate safety guards, task specific systems and processes and most importantly empowered people aligned in creating an industry leading safety culture. We do not accept shortcuts and are unwilling to employ or engage with anyone who is not aligned with this safety vision.</p>
    <p>We are a company that wants to enjoy our days work, and while we all have challenging days we believe we are stronger together. This message helps foster an inclusive and supportive team culture that allows us all to take great satisfaction from our achievements and celebrate them as a team.</p>
  </div>

  <div class="call-label">Call Us</div>
  <div class="call-rule"></div>
  <div class="phone" style="top:680px">
    <div class="phone-num"><svg width="12" height="12" viewBox="0 0 12 12"><circle cx="6" cy="6" r="5.2" fill="none" stroke="var(--yellow)" stroke-width="1.2"/><path d="M4 3.4l1 1.1-.6.8c.4.8 1 1.4 1.8 1.8l.8-.6 1.1 1-.6 1c-2 0-4.2-2.2-4.2-4.2z" fill="var(--yellow)"/></svg>0400 118 262</div>
    <div class="phone-name">Daniel Ross</div>
  </div>
  <div class="phone" style="top:711px">
    <div class="phone-num"><svg width="12" height="12" viewBox="0 0 12 12"><circle cx="6" cy="6" r="5.2" fill="none" stroke="var(--yellow)" stroke-width="1.2"/><path d="M4 3.4l1 1.1-.6.8c.4.8 1 1.4 1.8 1.8l.8-.6 1.1 1-.6 1c-2 0-4.2-2.2-4.2-4.2z" fill="var(--yellow)"/></svg>0411 520 347</div>
    <div class="phone-name">Martin Kell</div>
  </div>
  <ul class="contact-list">
    <li><svg width="10" height="8" viewBox="0 0 10 8"><rect x=".5" y=".5" width="9" height="7" fill="none" stroke="#555"/><path d="M.5.5l4.5 4 4.5-4" fill="none" stroke="#555"/></svg>tenders@twgroundworks.com.au</li>
    <li><svg width="10" height="10" viewBox="0 0 10 10"><circle cx="5" cy="5" r="4.4" fill="none" stroke="#555"/><ellipse cx="5" cy="5" rx="2" ry="4.4" fill="none" stroke="#555"/><path d="M.6 5h8.8" stroke="#555"/></svg>twgroundworks.com.au</li>
    <li><svg width="10" height="12" viewBox="0 0 10 12"><path d="M5 11.5S1 7 1 4.5a4 4 0 018 0C9 7 5 11.5 5 11.5z" fill="var(--navy)"/><circle cx="5" cy="4.5" r="1.5" fill="#fff"/></svg>4/18 Harlow Street, Northvale</li>
    <li class="indent">VIC 3061</li>
  </ul>
</section>

<section class="page page-back" aria-label="Capability statement, page two">
  <svg class="shape" width="539" height="761" viewBox="0 0 539 761">
    <defs>
      <linearGradient id="servicesTone" x1="0" y1="0" x2="1" y2="1">
        <stop offset="0" stop-color="#28247a"/>
        <stop offset=".6" stop-color="#2f2f8f"/>
        <stop offset="1" stop-color="#3a3fa8"/>
      </linearGradient>
      <linearGradient id="wedgeTone" x1="0" y1="0" x2="1" y2="0">
        <stop offset="0" stop-color="#f0b323"/>
        <stop offset=".5" stop-color="#c9921a"/>
        <stop offset="1" stop-color="#f0b323"/>
      </linearGradient>
    </defs>
    <polygon role="img" aria-label="Faint photo of excavation machinery behind the services list" points="0,0 539,0 539,256 76,347 0,317" fill="url(#servicesTone)"/>
    <polygon points="338,306 539,264 539,347" fill="url(#wedgeTone)"/>
    <polygon points="0,660 232,660 275,753 0,753" fill="var(--navy)"/>
    <rect x="0" y="753" width="539" height="8" fill="var(--navy)"/>
  </svg>

  <div class="services-bar">SERVICES</div>

  <div class="svc-col" style="left:42px;width:170px">
    <h3>Water Infrastructure</h3>
    <ul>
      <li>Accredited contractor with major Water Authorities</li>
      <li>Constructability design reviews from highly experienced professionals</li>
      <li>Reticulation mains and larger pipelines</li>
      <li>Experienced with PVC, Polyethylene, Ductile Iron, GRP and Mild Steel</li>
      <li>Butt welding of PE pipelines</li>
      <li>Domestic water services</li>
      <li>Meter assemblies</li>
      <li>Relocation of existing water assets</li>
      <li>Dedicated commissioning crew for Swabbing,</li>
      <li>Hydrostatic Testing, Chlorinating and Water</li>
      <li>Quality Testinglive connections</li>
    </ul>
  </div>
  <div class="svc-col" style="left:213px;width:158px">
    <h3>Water Infrastructure</h3>
    <ul>
      <li>Accredited contractor that can work on major Gas</li>
      <li>Authorities networks</li>
      <li>Constructability design reviews from highly<br>experienced professionals</li>
      <li>Reticulation mains in single or common trench and larger pipelines</li>
      <li>Butt welding and electro-fusion</li>
      <li>Pre-laid gas services</li>
      <li>Pressure testing</li>
      <li>Complex gas tie-ins</li>
    </ul>
  </div>
  <div class="svc-col" style="left:378px;width:150px">
    <h3>Water Infrastructure</h3>
    <ul>
      <li>Bulk earthworks</li>
      <li>Rehabilitation works</li>
      <li>Detailed excavations</li>
      <li>Hydro Excavation and underground service locating</li>
      <li>Landscaping</li>
      <li>General Civil works</li>
    </ul>
  </div>

  <div class="why">Why<br><span class="accent">choose</span><br>us ?</div>
  <div class="why-rule"></div>

  <div class="pillar" style="left:152px">
    <div class="pillar-badge"><svg width="34" height="34" viewBox="0 0 34 34" fill="none" stroke="#fff" stroke-width="2.2" stroke-linecap="round" stroke-linejoin="round"><circle cx="17" cy="17" r="12"/><path d="M11 17.5l4 4 8-8"/></svg></div>
    <div class="pillar-name">Trusted<br>Professionals</div>
  </div>
  <div class="pillar-link" style="left:242px"></div>
  <div class="pillar" style="left:235px">
    <div class="pillar-badge"><svg width="34" height="34" viewBox="0 0 34 34" fill="none" stroke="#fff" stroke-width="2.2" stroke-linecap="round" stroke-linejoin="round"><path d="M17 4l11 4v8c0 7-5 11.5-11 14-6-2.5-11-7-11-14V8z"/><path d="M12 17l4 4 7-7"/></svg></div>
    <div class="pillar-name">Safety<br>Focused</div>
  </div>
  <div class="pillar-link" style="left:325px"></div>
  <div class="pillar" style="left:319px">
    <div class="pillar-badge"><svg width="34" height="34" viewBox="0 0 34 34" fill="none" stroke="#fff" stroke-width="2.2" stroke-linecap="round" stroke-linejoin="round"><circle cx="17" cy="14" r="9"/><path d="M12 22l-3 9 5-2 3 4 3-4 5 2-3-9"/><path d="M13 14l3 3 5-5"/></svg></div>
    <div class="pillar-name">Quality<br>Assurance</div>
  </div>
  <div class="pillar-link" style="left:409px"></div>
  <div class="pillar" style="left:403px">
    <div class="pillar-badge"><svg width="34" height="34" viewBox="0 0 34 34" fill="none" stroke="#fff" stroke-width="2.2" stroke-linecap="round" stroke-linejoin="round"><circle cx="17" cy="17" r="6"/><path d="M17 4v4M17 26v4M4 17h4M26 17h4M8 8l3 3M23 23l3 3M26 8l-3 3M11 23l-3 3"/></svg></div>
    <div class="pillar-name">Collaborative<br>Problem Solvers</div>
  </div>

  <div class="focus-box"></div>
  <div class="focus-rule"></div>
  <div class="focus" style="left:59px">
    <h4>UTILITIES</h4>
    <p>Our team has a wide-ranging utilities background which gives us a deep understanding of what is in the ground and the specific requirements for each individual asset. Through this experience we have developed relationships with asset owners and distributors to ensure we deliver projects that will stand the test of time and be valuable pieces of future networks. Our commitment to safety and quality has further strengthened these relationships and puts us in a position to be a trusted advisor when the inevitable challenges are faced.</p>
  </div>
  <div class="focus" style="left:289px">
    <h4>CIVIL CONSTRUCTION</h4>
    <p>Leveraging off our considerable utilities background, we have seen our civil construction offering continue to grow. We have a resource base of skilled operators who take immense pridein their work and enable us to deliver cost effective, efficient services. We maintain a‘Tier 1’ mindset and hold ourselves to the highest standards, while still being an agile delivery partner that can be relied upon to deliver your next civil project</p>
  </div>

  <div class="call-label">Call Us</div>
  <div class="call-rule"></div>
  <div class="phone" style="top:680px">
    <div class="phone-num"><svg width="12" height="12" viewBox="0 0 12 12"><circle cx="6" cy="6" r="5.2" fill="none" stroke="var(--yellow)" stroke-width="1.2"/><path d="M4 3.4l1 1.1-.6.8c.4.8 1 1.4 1.8 1.8l.8-.6 1.1 1-.6 1c-2 0-4.2-2.2-4.2-4.2z" fill="var(--yellow)"/></svg>0400 118 262</div>
    <div class="phone-name">Daniel Ross</div>
  </div>
  <div class="phone" style="top:711px">
    <div class="phone-num"><svg width="12" height="12" viewBox="0 0 12 12"><circle cx="6" cy="6" r="5.2" fill="none" stroke="var(--yellow)" stroke-width="1.2"/><path d="M4 3.4l1 1.1-.6.8c.4.8 1 1.4 1.8 1.8l.8-.6 1.1 1-.6 1c-2 0-4.2-2.2-4.2-4.2z" fill="var(--yellow)"/></svg>0411 520 347</div>
    <div class="phone-name">Martin Kell</div>
  </div>
  <ul class="contact-list">
    <li><svg width="10" height="8" viewBox="0 0 10 8"><rect x=".5" y=".5" width="9" height="7" fill="none" stroke="#555"/><path d="M.5.5l4.5 4 4.5-4" fill="none" stroke="#555"/></svg>tenders@twgroundworks.com.au</li>
    <li><svg width="10" height="10" viewBox="0 0 10 10"><circle cx="5" cy="5" r="4.4" fill="none" stroke="#555"/><ellipse cx="5" cy="5" rx="2" ry="4.4" fill="none" stroke="#555"/><path d="M.6 5h8.8" stroke="#555"/></svg>twgroundworks.com.au</li>
    <li><svg width="10" height="12" viewBox="0 0 10 12"><path d="M5 11.5S1 7 1 4.5a4 4 0 018 0C9 7 5 11.5 5 11.5z" fill="var(--navy)"/><circle cx="5" cy="4.5" r="1.5" fill="#fff"/></svg>4/18 Harlow Street, Northvale</li>
    <li class="indent">VIC 3061</li>
  </ul>
</section>

</body>
</html>
```